TK Joinery

Cabinet maker. Kitchens. Wardrobes. Vanitys. Entertainment units

Target Market(s)

Modern contemporary.geometry. colours black, gray, charcoal and orange. Matt card gloss letters

Industry/Entity Type

Entertainment

Contact Information for Business Card

Marcel Otvany 0417 382 594
marcel.otvany@fernmail.test
ABN 731 4928 5170

Font styles to use
Decorative

Colors
000000

Requirements
Should not have
• Pictures

```html
<!DOCTYPE html>
<html lang="en">
<head>
<meta charset="utf-8">
<title>TK Joinery — Business Card</title>
<link href="https://fonts.googleapis.com/css2?family=Federant&display=swap" rel="stylesheet">
<style>
  :root {
    --page: #e9e5de;
    --card: #000000;
    --ink: #ffffff;
  }
  * { margin: 0; padding: 0; box-sizing: border-box; }
  html, body {
    width: 1200px; height: 1200px; overflow: hidden;
    background: var(--page);
    font-family: "Federant", serif;
    color: var(--ink);
  }
  .card {
    position: absolute;
    left: 238px;
    width: 722px;
    height: 444px;
    background: var(--card);
  }
  .card--front { top: 134px; }
  .card--back { top: 622px; }

  .front-frame {
    position: absolute;
    left: 56px; top: 56px;
    width: 610px; height: 332px;
    border: 2.5px solid var(--ink);
    display: flex; align-items: center; justify-content: center;
  }
  .brand-name {
    font-size: 58px;
    font-weight: 400;
    letter-spacing: 4px;
    text-transform: uppercase;
    margin-bottom: 26px;
  }

  .services {
    position: absolute;
    left: 0; top: 112px;
    list-style: none;
  }
  .services li {
    display: flex; align-items: center;
    height: 45px;
    font-size: 22px;
  }
  .services .bullet { width: 30px; height: 16px; margin-right: 13px; flex: none; }

  .owner-name {
    position: absolute;
    right: 64px; top: 100px;
    font-size: 38px;
    font-weight: 400;
  }
  .contacts {
    position: absolute;
    right: 58px; top: 256px;
    list-style: none;
  }
  .contacts li {
    display: flex; align-items: center; justify-content: flex-end;
    height: 46px;
    font-size: 21px;
  }
  .contacts .icon {
    width: 20px; height: 22px;
    margin-left: 22px; flex: none;
    display: flex; align-items: center; justify-content: center;
    font-size: 20px;
  }
</style>
</head>
<body>
  <section class="card card--front">
    <div class="front-frame">
      <h1 class="brand-name">TK Joinery</h1>
    </div>
  </section>

  <section class="card card--back">
    <ul class="services">
      <li><svg class="bullet" viewBox="0 0 30 16"><path d="M2 7 Q2 3 8 2 L28 0 Q30 6 27 10 L4 16 Q0 14 2 7 Z" fill="#fff"/></svg>Cabinet maker</li>
      <li><svg class="bullet" viewBox="0 0 30 16"><path d="M2 7 Q2 3 8 2 L28 0 Q30 6 27 10 L4 16 Q0 14 2 7 Z" fill="#fff"/></svg>Kitchens</li>
      <li><svg class="bullet" viewBox="0 0 30 16"><path d="M2 7 Q2 3 8 2 L28 0 Q30 6 27 10 L4 16 Q0 14 2 7 Z" fill="#fff"/></svg>Wardrobes</li>
      <li><svg class="bullet" viewBox="0 0 30 16"><path d="M2 7 Q2 3 8 2 L28 0 Q30 6 27 10 L4 16 Q0 14 2 7 Z" fill="#fff"/></svg>Vanitys</li>
      <li><svg class="bullet" viewBox="0 0 30 16"><path d="M2 7 Q2 3 8 2 L28 0 Q30 6 27 10 L4 16 Q0 14 2 7 Z" fill="#fff"/></svg>Entertainment units</li>
    </ul>

    <h2 class="owner-name">Marcel Otvany</h2>

    <ul class="contacts">
      <li>0417 382 594
        <span class="icon"><svg width="12" height="20" viewBox="0 0 12 20"><path d="M3 1 L6 1 L6 6 L4 7 Q4 11 7 14 L9 13 L11 17 L8 19 Q1 14 1 5 Q1 2 3 1 Z" fill="#fff"/></svg></span>
      </li>
      <li>marcel.otvany@fernmail.test
        <span class="icon">@</span>
      </li>
      <li>ABN 731 4928 5170
        <span class="icon"><svg width="14" height="22" viewBox="0 0 14 22"><path d="M7 1 A6 6 0 0 1 13 7 Q13 12 7 21 Q1 12 1 7 A6 6 0 0 1 7 1 Z M7 4.5 A2.5 2.5 0 1 0 7 9.5 A2.5 2.5 0 1 0 7 4.5 Z" fill="#fff" fill-rule="evenodd"/></svg></span>
      </li>
    </ul>
  </section>
</body>
</html>
```